Design our branded business card!

We'd love for you to design our business card and come up with a fitting design that reflects the Brimble brand. We're a growing tech startup with big ambitions. We've included our brand guidelines (contain colour palette), logo (EPS vector in CMYK) and old designs to help you on your way.

We'd like to keep the design fairly simple:

* Name
* Phone number
* Email address
* Website (www.brimble.life)
* Twitter (@brimble)
* Address (19 Fenwick Row, Leeds, UK, LS4 9QT).

This would need to include print and cutting marks.

If you have any questions just let us know!

Target Market(s)

Businesses, Press and our customers!

Industry/Entity Type

Business

Contact Information for Business Card

* Name
* Phone number
* Email address
* Twitter (@brimble)

Font styles to use
Sans Serif

Requirements
Must have
• 1. Must have the Brimble logo included.
• 2. Must use the font 'Brandon Text' in either 'light' or 'thin' (https://www.typevaultex.com/fonts/qrnfoundry/brandon-text/)
• 3. Must use exact colours references from the brand guidelines. Colours outside of the brand guidelines will be discounted. White (transparent) backgrounds are fine.
• 4. Must contain the following information:
• * Name
• * Phone number
• * Email address
• * Website (www.brimble.life)
• * Twitter (@brimble)
• * Address (19 Fenwick Row, Leeds, UK, LS4 9QT).
Nice to have
• Must use the font 'Brandon Text' in either 'light' or 'thin' (https://www.typevaultex.com/fonts/qrnfoundry/brandon-text/)
Should not have
• Colours outside of the brand guidelines will be discounted. White (transparent) backgrounds are fine.
• Avoid creating icons or including photography.

```html
<!DOCTYPE html>
<html lang="en">
<head>
<meta charset="utf-8">
<title>Brimble business card</title>
<link rel="stylesheet" href="https://fonts.googleapis.com/css2?family=Mulish:wght@300;400;600&display=swap">
<style>
  :root {
    --backdrop: #474747;
    --charcoal: #3a4442;
    --leaf: #7dc472;
    --leaf-faint: #e6f2e3;
    --paper: #ffffff;
    --ink-light: #f2f4f3;
  }
  * { margin: 0; padding: 0; box-sizing: border-box; }
  html, body {
    width: 1105px;
    height: 1200px;
    overflow: hidden;
    background: var(--backdrop);
    font-family: "Mulish", sans-serif;
  }
  .card {
    position: absolute;
    left: 196px;
    width: 720px;
    height: 412px;
    overflow: hidden;
  }
  .card--front { top: 146px; background: var(--charcoal); }
  .card--back { top: 602px; background: var(--paper); }

  .front-disc {
    position: absolute;
    left: 510px;
    top: -6px;
    width: 410px;
    height: 410px;
    border-radius: 50%;
    background: var(--leaf);
  }
  .wordmark {
    position: absolute;
    font-weight: 300;
    letter-spacing: 1px;
    line-height: 1;
  }
  .card--front .wordmark {
    left: 56px;
    top: 52px;
    font-size: 58px;
    color: var(--paper);
  }
  .holder-name {
    position: absolute;
    left: 57px;
    top: 140px;
    font-size: 30px;
    font-weight: 600;
    color: var(--leaf);
  }
  .address {
    position: absolute;
    left: 58px;
    top: 186px;
    font-size: 19px;
    font-weight: 400;
    line-height: 30px;
    color: var(--ink-light);
    font-style: normal;
  }
  .contacts {
    position: absolute;
    left: 58px;
    top: 255px;
    list-style: none;
  }
  .contacts li {
    display: flex;
    align-items: center;
    height: 28px;
    font-size: 18px;
    color: var(--ink-light);
  }
  .contacts svg {
    width: 17px;
    height: 17px;
    margin-right: 14px;
    fill: var(--leaf);
    flex: none;
  }

  .back-disc {
    position: absolute;
    left: -207px;
    top: -1px;
    width: 414px;
    height: 414px;
    border-radius: 50%;
    background: var(--leaf-faint);
  }
  .back-lockup {
    position: absolute;
    left: 287px;
    top: 162px;
    display: flex;
    align-items: center;
  }
  .back-lockup .dot {
    width: 97px;
    height: 97px;
    border-radius: 50%;
    background: var(--leaf);
    margin-right: 18px;
  }
  .card--back .wordmark {
    position: static;
    font-size: 62px;
    color: var(--charcoal);
  }
</style>
</head>
<body>
  <section class="card card--front">
    <div class="front-disc"></div>
    <div class="wordmark">Brimble</div>
    <div class="holder-name">Harriet Vale</div>
    <address class="address">19 Fenwick Row<br>Leeds, UK, LS4 9QT</address>
    <ul class="contacts">
      <li>
        <svg viewBox="0 0 24 24" aria-hidden="true"><path d="M6.6 10.8c1.4 2.8 3.8 5.1 6.6 6.6l2.2-2.2c.3-.3.7-.4 1-.2 1.1.4 2.3.6 3.6.6.6 0 1 .4 1 1V20c0 .6-.4 1-1 1C10.6 21 3 13.4 3 4c0-.6.4-1 1-1h3.5c.6 0 1 .4 1 1 0 1.3.2 2.5.6 3.6.1.3 0 .7-.2 1l-2.3 2.2z"/></svg>
        604 318 2719
      </li>
      <li>
        <svg viewBox="0 0 24 24" aria-hidden="true"><path d="M2 5h20v2l-10 6L2 7V5zm0 4.3l10 6 10-6V19H2V9.3z"/></svg>
        name@brimble.life
      </li>
      <li>
        <svg viewBox="0 0 24 24" aria-hidden="true"><path d="M12 2a10 10 0 1 0 0 20 10 10 0 0 0 0-20zm-1 17.9A8 8 0 0 1 4.2 10.2L9 15v1c0 1.1.9 2 2 2v1.9zm6.9-2.5c-.3-.8-1-1.4-1.9-1.4h-1v-3c0-.6-.4-1-1-1H8v-2h2c.6 0 1-.4 1-1V7h2c1.1 0 2-.9 2-2v-.4a8 8 0 0 1 2.9 12.8z"/></svg>
        www.brimble.life
      </li>
      <li>
        <svg viewBox="0 0 24 24" aria-hidden="true"><circle cx="12" cy="12" r="8"/></svg>
        @brimble
      </li>
    </ul>
  </section>

  <section class="card card--back">
    <div class="back-disc"></div>
    <div class="back-lockup">
      <div class="dot"></div>
      <div class="wordmark">Brimble</div>
    </div>
  </section>
</body>
</html>
```